Multifamily Investment Strategies

I need a pamphlet or booklet for multifamily commercial real estate investment.

The specific investment vehicle is affordable multifamily apartments. I have uploaded a 5 page pdf detailing my investment strategy.

The target audience for this pamphlet are investors, commercial brokers, and commercial bankers.

I am looking for modern, clean design that is striking and professional but also eye catching.
Updates

I made a few changes to the brief and also corrected two errors.

Target Market(s)

Commercial Real Estate Investors, Brokers, and Bankers

Industry/Entity Type

Real Estate

Font styles to use
Serif

Colors

Designer to choose colors to be used in the design.

Requirements
Must have
• Graphics of or related to apartment buildings.
• My headshot seen on the last page of the pdf
Nice to have
• Imagery related to investment and profits.
Should not have
• The image of an apartment building on the first page of the pdf is just an example. Please don’t use this image.

```html
<!DOCTYPE html>
<html lang="en">
<head>
<meta charset="utf-8">
<title>Multifamily Cashflow Investment Strategy – Booklet Pages</title>
<link href="https://fonts.googleapis.com/css2?family=Roboto:wght@400;500;700;900&family=Roboto+Condensed:wght@400;700&family=Libre+Baskerville:wght@400;700&display=swap" rel="stylesheet">
<style>
  :root {
    --stage: #5f7070;
    --blue: #2f8fc6;
    --blue-dark: #1f6fa3;
    --ink: #2b2f33;
    --ink-soft: #555b61;
    --paper: #ffffff;
    --paper-tint: #f1f4f7;
    --label: #ffffff;
  }
  * { box-sizing: border-box; margin: 0; padding: 0; }
  html, body { width: 1200px; height: 1200px; overflow: hidden; }
  body {
    position: relative;
    background: var(--stage);
    font-family: "Roboto", Arial, sans-serif;
    color: var(--ink);
  }
  .page-label {
    position: absolute;
    color: var(--label);
    font-family: "Roboto", Arial, sans-serif;
    font-weight: 700;
    font-size: 26px;
    letter-spacing: 0.2px;
    white-space: nowrap;
  }
  .page {
    position: absolute;
    background: var(--paper);
    overflow: hidden;
  }
  .abs { position: absolute; }
  .photo { position: absolute; }
  .bottom-bar { position: absolute; left: 0; right: 0; bottom: 0; height: 5px; background: var(--blue); }

  .copy { font-family: "Roboto", Arial, sans-serif; font-size: 3.6px; line-height: 4.6px; color: var(--ink-soft); }
  .copy .h { color: var(--ink); font-weight: 700; font-size: 4px; display: block; margin-top: 3px; }
  .copy .h-blue { color: var(--blue); font-weight: 500; font-size: 4px; display: block; margin-top: 4px; }
  .copy p { margin: 0.5px 0 0 6px; text-align: justify; }
  .copy ul { list-style: none; margin-left: 6px; }
  .copy li { margin-top: 0.4px; }

  .cover { left: 466px; top: 74px; width: 281px; height: 364px; }
  .cover-title {
    position: absolute; left: 0; right: 0; top: 15px; text-align: center;
    font-family: "Roboto Condensed", Arial, sans-serif; font-weight: 700;
    font-size: 11px; color: var(--blue);
  }
  .cover-stripe { position: absolute; left: 0; right: 0; top: 39px; height: 5px; background: var(--blue); }
  .cover-photo {
    left: 0; top: 44px; width: 281px; height: 256px;
    background:
      radial-gradient(ellipse at 55% 75%, rgba(255,170,60,0.55), transparent 45%),
      linear-gradient(180deg, #2f6fcf 0%, #5b9be8 35%, #8cc0ee 55%, #2a3f66 80%, #1b2436 100%);
  }
  .cover-foot-tri { position: absolute; right: 0; top: 262px; }
  .cover-sub {
    position: absolute; left: 15px; top: 316px;
    font-family: "Roboto Condensed", Arial, sans-serif; font-weight: 700;
    font-size: 10px; line-height: 11.5px; color: var(--ink);
  }
  .cover-url {
    position: absolute; left: 96px; top: 344px;
    font-size: 7px; font-weight: 500; color: var(--blue);
  }

  .p1 { left: 274px; top: 477px; width: 250px; height: 320px; }
  .steps-block {
    position: absolute; left: 0; top: 0; width: 111px; height: 103px; background: var(--blue);
    color: #fff; font-family: "Libre Baskerville", Georgia, serif; font-weight: 700; text-align: center;
    padding-top: 36px;
  }
  .steps-block .big { font-size: 19px; line-height: 20px; letter-spacing: 0.5px; }
  .steps-block .small { font-size: 12px; line-height: 17px; letter-spacing: 0.5px; }
  .p1-col-right { position: absolute; left: 111px; top: 93px; width: 139px; height: 222px; background: var(--paper-tint); }

  .section-title {
    position: absolute; font-family: "Libre Baskerville", Georgia, serif; font-size: 6.2px;
    color: var(--blue); letter-spacing: 0.2px; text-transform: uppercase; white-space: nowrap;
  }
  .framed { border: 1px solid var(--blue-dark); }

  .p4-title {
    position: absolute; left: 0; right: 0; top: 183px; text-align: center;
    font-family: "Roboto", Arial, sans-serif; font-weight: 500; font-size: 6.5px; letter-spacing: 0.2px; color: var(--ink);
  }
  .about-head { position: absolute; left: 99px; top: 212px; font-size: 8px; color: var(--blue); font-weight: 500; }
  .about-copy { position: absolute; left: 99px; top: 228px; width: 127px; font-size: 3.5px; line-height: 4.3px; color: var(--ink-soft); text-align: justify; }
  .about-name { position: absolute; left: 99px; top: 271px; font-size: 7.5px; color: var(--blue); font-weight: 500; }
  .about-role { position: absolute; left: 99px; top: 282px; font-size: 5.6px; color: var(--ink); }
</style>
</head>
<body>

<div class="page-label" style="left:534px; top:30px;">Front Page</div>

<section class="page cover">
  <svg class="abs" style="left:0;top:0" width="24" height="20" viewBox="0 0 24 20"><polygon points="0,0 24,0 0,20" fill="var(--blue)"/></svg>
  <div class="cover-title">Multifamily Cashflow Investment Strategy</div>
  <div class="cover-stripe"></div>
  <div class="photo cover-photo" role="img" aria-label="Modern glass apartment tower lit at dusk beside a waterfront promenade"></div>
  <svg class="abs" style="left:0;top:298px" width="281" height="8" viewBox="0 0 281 8"><rect width="281" height="4" fill="var(--blue)"/></svg>
  <svg class="cover-foot-tri" width="60" height="102" viewBox="0 0 60 102"><polygon points="60,0 60,102 0,102 48,14" fill="var(--blue)"/></svg>
  <div class="cover-sub">Turning Underperforming Multifamily Properties<br>into Highly Profitable, Cash Flowing Assets</div>
  <div class="cover-url">www.xxxx.co.in</div>
</section>

<div class="page-label" style="left:152px; top:624px;">1st Page</div>
<div class="page-label" style="left:934px; top:606px;">2nd Page</div>
<div class="page-label" style="left:152px; top:984px;">3rd Page</div>
<div class="page-label" style="left:934px; top:998px;">4th Page</div>

<section class="page p1">
  <div class="steps-block"><div class="big">3 STEPS</div><div class="small">FOR<br>SUCCESS</div></div>
  <div class="photo" style="left:111px;top:0;width:139px;height:93px;background:linear-gradient(135deg,#f4e9dc 0%,#e2c9a6 45%,#b86a52 70%,#8a9a64 100%);" role="img" aria-label="Small house model on stacks of coins with a growing plant"></div>
  <div class="p1-col-right"></div>
  <div class="photo" style="left:0;top:215px;width:111px;height:100px;background:linear-gradient(180deg,#d9cfc2 0%,#9c8672 45%,#5c4a3d 75%,#3a2f29 100%);" role="img" aria-label="Warm modern apartment living room interior"></div>

  <div class="abs copy" style="left:9px;top:110px;width:96px;">
    <span class="h">1. Buy Right:</span>
    <span class="h-blue">✓ Value Add</span>
    <p>Key questions when considering a property:</p>
    <ul><li>- Who owns it?</li><li>- How long have they owned it?</li><li>- Why are they selling it?</li></ul>
    <span class="h-blue">✓ What to look for:</span>
    <span class="h" style="margin-left:6px">A. Poor management -</span>
    <p style="margin-left:14px">Typically by individual owners, families, or out of state management.</p>
    <span class="h" style="margin-left:6px">B. Under market rents -</span>
    <p style="margin-left:14px">Rates significantly below comparable prices in the area.</p>
  </div>

  <div class="abs copy" style="left:115px;top:95px;width:130px;">
    <span class="h" style="margin-top:0">C. Deferred maintenance -</span>
    <p>This can be a sign of a motivated or burned-out seller. Light exterior and interior upgrades, e.g., paint, landscaping, carpet replacement, fixture and appliance upgrades, will have a significant impact.</p>
    <span class="h">D. High vacancy -</span>
    <p>Often due to poor marketing.</p>
    <span class="h">E. Motivated sellers -</span>
    <p>Allows for negotiation a lower price. Common motivators include divorce, bankruptcy, retirement, inherited properties, new investment opportunity, burnout, etc.</p>
    <span class="h">F. Owner paid utilities -</span>
    <p>Allows for significant upside in income through implementing Ratio Utility Business System (RUBS).</p>
    <p>- By tackling these issues, we will successfully reposition the property, which will significantly increase the income. As a result, the value of the property will also increase.</p>
    <span class="h-blue">✓ Property Class -</span>
    <p>B and C class properties in A and B neighborhoods - Prefer 1980's or newer.</p>
    <p style="margin-left:10px;margin-top:3px">- These properties tend to house blue collar workers; don't compete with newest construction; and don't share the same challenges as C and D properties in C and D neighborhoods, which can encounter issues with crime, major disrepair, and increased vulnerability to economic downturns.</p>
    <span class="h-blue">✓ Market Analysis -</span>
    <p>Target emerging markets with population and job growth; low to median cost of housing which allows rent growth (e.g., Columbus, Oklahoma, Atlanta, Dallas, Phoenix); median income of ~$55k/yr; and landlord and business friendly rules and regulations (e.g., Ohio, Texas, Florida, Oklahoma, Colorado).</p>
  </div>
  <div class="bottom-bar"></div>
</section>

<section class="page" style="left:670px;top:477px;width:248px;height:320px;">
  <div class="photo" style="left:0;top:0;width:248px;height:153px;background:linear-gradient(180deg,#cfd9e6 0%,#b9b4a6 40%,#8a7a62 65%,#3f3a33 82%,#2a2e34 100%);" role="img" aria-label="Waterfront apartment buildings with balconies at dusk"></div>
  <div class="abs copy" style="left:12px;top:156px;width:226px;">
    <span class="h-blue" style="margin-top:0">✓ Scale -</span>
    <p>60+ units to support effective, third-party professional management. Additionally, targeting 60+ units will increase the likelihood of stability by creating a buffer against tenant turnover and other unplanned expenses.</p>
    <span class="h-blue">✓ Cash flow -</span>
    <p>The property must generate cash flow from day one, before value add strategies are deployed.</p>
    <p style="margin-top:5px;margin-left:0">✓ Buy on actual numbers instead of on pro forma analysis, which project or estimate financial return.</p>
    <span class="h" style="margin-top:6px">2. Finance Right:</span>
    <ul>
      <li>• Long-term debt - with long terms and amortization periods.</li>
      <li>• Non-recourse if possible, e.g., Harbor Home Lending, Northgate Mortgage, CMBS. There is an extremely low foreclosure rate for agency underwritten properties (1%-2%).</li>
      <li>• No prepayment penalty.</li>
      <li>• No due on sale clause.</li>
    </ul>
    <span class="h" style="margin-top:6px">3. Manage Right:</span>
    <ul>
      <li>• Third Party Management with experience in this specific class of multifamily real estate.</li>
      <li style="margin-left:6px">• Sizable but not too large that our property gets lost.</li>
      <li style="margin-left:6px">• Only in property management, not acquisition or development so that there is no conflict of interest.</li>
      <li>• Use of Sole Purpose Entity Structures, e.g., LLC's for asset protection.</li>
      <li>• Optimization through use of systems.</li>
      <li>• Tenant satisfaction - Ensure great customer service to the tenant, e.g., 24 hour response to maintenance requests, cleanliness, and security. Happy tenants who feel heard and cared for, don't leave, which limits tenant turnover, and lowers expenses.</li>
      <li>• Increase the "curb appeal" - Freshened exterior with modern paint schemes, landscaping, and new signage. Rebranding with a name change, webpage, etc.</li>
    </ul>
  </div>
  <div class="bottom-bar"></div>
</section>

<section class="page" style="left:274px;top:841px;width:250px;height:322px;">
  <div class="section-title" style="left:6px;top:12px;">› 5 Strategies for Increasing Income</div>
  <div class="photo framed" style="left:6px;top:27px;width:108px;height:83px;background:linear-gradient(180deg,#cfe3f2 0%,#c9a68f 40%,#8a6b58 60%,#5f9a3a 80%,#c4b59a 100%);" role="img" aria-label="Apartment complex with lawn and paved walkway"></div>
  <div class="abs copy" style="left:125px;top:44px;width:118px;">
    <span class="h-blue" style="margin-top:0">1. Fill vacant units at market rate</span>
    <p>After light renovation (&lt; $1,000 per unit) - modern, two-tone paint schemes (white trim, taupe/light grey walls); vinyl wood plank flooring to replace carpet, cleaning of existing carpet.</p>
    <span class="h-blue" style="margin-top:5px">2. Employ RUBS, where applicable</span>
    <p>Pre-calculated formula for billing back a tenant's utilities. Water, sewer, trash, gas/electric.</p>
  </div>
  <div class="abs copy" style="left:11px;top:137px;width:116px;">
    <span class="h-blue" style="margin-top:0">3. Gradually raise existing tenants to market rate AFTER adding value</span>
    <p>Improve the exterior "curb appeal" - power washing, landscaping, painting. Inexpensive and effective.</p>
    <span class="h-blue">4. Fees - Pet fees; deposits; late fees (without exception); move-in fees</span>
    <span class="h-blue">5. Laundry machines</span>
    <span class="h-blue">6. Lower expenses through renegotiation of contracts</span>
  </div>
  <div class="photo framed" style="left:130px;top:127px;width:108px;height:82px;background:linear-gradient(180deg,#f2d9a0 0%,#c9a062 35%,#7d6a45 60%,#4d5b34 85%,#3a4a2a 100%);" role="img" aria-label="Mid-rise apartment building in golden evening light"></div>
  <div class="section-title" style="left:6px;top:224px;">› 5 Ways to Profit</div>
  <div class="abs copy" style="left:18px;top:238px;width:224px;">
    <p style="margin:0">1. Monthly Cash Flow - from day one. Conservative estimation of 9% or higher cash on cash returns.</p>
    <p style="margin:2px 0 0">2. Equity through principle pay down - As the tenants pay down the mortgage, your equity continues to increase and creates true wealth.</p>
    <p style="margin:2px 0 0">3. Reduced or even elimination of taxes through depreciation by doing cost segregation.</p>
    <p style="margin:2px 0 0">4. Cash out refinancing - into non-recourse debt (if not already); return of original capital plus additional monies that can be used towards reinvestment into the asset and future assets.</p>
    <p style="margin:2px 0 0">5. Forced Appreciation - by repositioning the asset through the methods previously discussed. Potential to double the original investment at the time of sale, which could occur in 5-7 years or sooner depending on the market.</p>
  </div>
  <div class="bottom-bar"></div>
</section>

<section class="page" style="left:669px;top:841px;width:250px;height:322px;">
  <div class="photo" style="left:0;top:0;width:250px;height:174px;background:linear-gradient(180deg,#2f7fd8 0%,#6eaee6 40%,#b89a78 60%,#5b5f5a 78%,#4f7a3a 92%,#9aa0a4 100%);" role="img" aria-label="Contemporary four-storey apartment building with wood accents under a blue sky"></div>
  <div class="abs" style="left:0;top:174px;width:250px;height:2px;background:var(--blue);"></div>
  <div class="p4-title">MULTIFAMILY CASHFLOW INVESTMENT STRATEGY</div>
  <div class="photo" style="left:23px;top:209px;width:63px;height:79px;background:linear-gradient(180deg,#e6e6e6 0%,#9a9a9a 55%,#5a5a5a 100%);" role="img" aria-label="Black and white headshot of the investor"></div>
  <div class="about-head">About me</div>
  <div class="about-copy">Maren Holloway is a residential real estate investor and physician with a passion for identifying and fixing problems through innovative and creative solutions. Her transition into commercial real estate is merely an extension of that passion. It is her professional experience in a demanding and competitive field, along with her tenacity and discipline for doing things effectively and efficiently, which instills confidence in her success as a CRE investor.</div>
  <div class="about-name">Maren Holloway</div>
  <div class="about-role">Residential Real Estate Investor</div>
  <div class="bottom-bar" style="height:7px"></div>
</section>

</body>
</html>
```